TAVRO Capital Group LLC a High Risk Big Rewards company for Rich Young Entrepreneurs

We would like a very modern, powerful in the eyes of our customers, modern, minimalist feel, financial gain. this business card is for young Rich entrepreneurs who want to invest money into High Risk, Big Rewards Businesses. The card Should sell the business!! let your creativity go Wild! I pick most of the designers for this project because of your BOLD Designs, I would like this card to be Bold, Modern, Minimalist, use as many effects in your graphic Artist Mind, Do not let the Financial sound of this business to make you think Conservative that's the last thing we are! if you have a lot of money and you want to play a risky market call US
Updates

Project Deadline Extended
Reason: have not received, enough designs to choose 1st and second place, sure I have received over 100 designs but it seems most designers are submitting every card they have ever made before and calling it mine, please we are looking for fresh ideas please!

Target Market(s)

Private Risky Investors

Industry/Entity Type

Financial

Contact Information for Business Card

powerful in the eyes of our customers,modern, minimalist feel

Font styles to use
Other font styles liked:
• Modern feeling fonts

Requirements
Must have
• The Company Name is TAVRO Capital Group LLC and it must be on the CARD
• My Name, title, Cell , email
• Delvin Ashcroft G.E.D.
• Managing Member
• 555.038.6195
• delvin@tavrocapitalgroup.example
Nice to have
• try a black thick plastic card with round corners with Delvin Ashcroft GED (make sure GED is smaller than name) just on one side of the card, and my phone number with out the icons and email on the other side, this card should look like a exclusive credit card or exclusive VIP card, something you would never loose

```html
<!DOCTYPE html>
<html lang="en">
<head>
<meta charset="utf-8">
<title>TAVRO Capital Group LLC — Business Card</title>
<link rel="stylesheet" href="https://fonts.googleapis.com/css2?family=Quicksand:wght@300;400&family=Didact+Gothic&family=Open+Sans:ital,wght@1,500&display=swap">
<style>
  :root {
    --page: #ffffff;
    --stage: #b2b5b6;
    --card: #ffffff;
    --ink: #011927;
    --on-ink: #ffffff;
    --accent: #5fb8e0;
  }
  html, body {
    margin: 0;
    width: 1200px;
    height: 1000px;
    overflow: hidden;
    background: var(--page);
  }
  .presentation { display: block; width: 1200px; height: 1000px; }
  .stage { fill: var(--stage); }
  .card-face { fill: var(--card); }
  .band { fill: var(--ink); }
  .company-name {
    font-family: "Quicksand", sans-serif;
    font-weight: 300;
    font-size: 31px;
    fill: var(--on-ink);
  }
  .company-tagline {
    font-family: "Quicksand", sans-serif;
    font-weight: 400;
    font-size: 21px;
    fill: var(--accent);
  }
  .holder-name {
    font-family: "Didact Gothic", sans-serif;
    font-size: 25px;
    fill: var(--on-ink);
  }
  .holder-title {
    font-family: "Open Sans", sans-serif;
    font-style: italic;
    font-weight: 500;
    font-size: 14px;
    letter-spacing: 1.6px;
    fill: var(--on-ink);
  }
  .contact {
    font-family: "Didact Gothic", sans-serif;
    font-size: 23px;
    fill: var(--ink);
  }
  .contact-phone { letter-spacing: 4px; }
  .contact-email { letter-spacing: 0.6px; }
</style>
</head>
<body>
<svg class="presentation" viewBox="0 0 1200 1000" xmlns="http://www.w3.org/2000/svg">
  <rect class="stage" x="38" y="35" width="1120" height="930"/>

  <!-- Front of card -->
  <g class="card card-front">
    <rect class="card-face" x="277" y="132" width="590" height="336"/>
    <polygon class="band" points="812,132 867,132 867,200 345,468 277,468 277,407"/>
    <g transform="translate(352 410) rotate(-27.2)">
      <text class="company-name" x="0" y="0" textLength="470" lengthAdjust="spacingAndGlyphs">TAVRO CAPITAL GROUP, LLC</text>
      <text class="company-tagline" x="40" y="24" textLength="420" lengthAdjust="spacingAndGlyphs">a Domestic Limited Liability Company</text>
    </g>
  </g>

  <!-- Back of card -->
  <g class="card card-back">
    <rect class="card-face" x="283" y="515" width="591" height="336"/>
    <path class="band" d="M283 515 H735 C700 560 680 605 560 605 H283 Z"/>
    <text class="holder-name" x="307" y="556">Delvin Ashcroft G.E.D.</text>
    <text class="holder-title" x="352" y="583">Managing Member</text>
    <text class="contact contact-phone" x="409" y="715">T:555.038.6195</text>
    <text class="contact contact-email" x="409" y="757">delvin@tavrocapitalgroup.example</text>
  </g>
</svg>
</body>
</html>
```